Junk Removal Website Design

We are working with a Junk Removal company in California. They provide junk hauling services for commercial and residential throughout California.
Some sites to use for inspiration:
https://www.clearbarrowhauls.com
https://pebblecartworkteam.com
https://www.fernwayliftersandmovers.com
https://www.mistoakcleanupcrew.com
Thank you for taking the time to consider designing a website for us. We are web developers based in Stockton, CA, USA. Most of our projects go through the same process. Understanding this process may help you win a project with us. We custom-code all of our websites in-house. We don’t have any requirements as to what tools you use for your design, but we ask that you follow these guidelines.
IMAGES:
If you use any images or icons in the design, we ask that you have a link to the asset so we can purchase the image/icon. Most of the designs we submit do not have the customer’s images on them unless they have some great images. Be creative; show us the feeling you are trying to portray with your image choices. Use any royalty-free site you choose. We subscribe to Vontrel and mainly use their images, but we can purchase images outside of Vontrel. PLEASE NOTE: we will not submit designs to clients with watermarks on the images.
FONTS:
We ask that you identify the fonts you’re using in the design. This can be done in a message if you want. We typically use Quimbly Fonts and Vontrel Fonts.
CONTENT:
We're always open to different content and ideas. We often submit designs with stock images so the client can see our vision. We typically take pictures after the website launch to use their images with our vision. Lorem Ipsum is fine for paragraphs, but we ask that you make the Headers with correct English. We want to be able to show the vision and identify the sections of the website.
INSPIRATION:
We typically add a couple of links in the brief of websites we like to help you get started in your design.
REVISIONS:
We do not often ask for revisions of the designs unless we see something in the design that may not appeal to the client. If there are slight changes that we want to make, we do that in the development process.
FEEDBACK:
We rarely give feedback on designs during the design process. We are working on many website projects and do not have the time to provide feedback. We usually respond if your request is well thought out and asks specific questions, but a note asking “feedback, please” usually goes unanswered.
Number of Pages Required
1 page

```html
<!DOCTYPE html>
<html lang="en">
<head>
<meta charset="utf-8">
<title>Junk Removal</title>
<link href="https://fonts.googleapis.com/css2?family=Barlow:wght@700;800;900&family=Roboto:wght@400;500;700&display=swap" rel="stylesheet">
<style>
:root{
  --green:#4c9f38;
  --green-dark:#3f8a2e;
  --ink:#1f1f1f;
  --dark:#262626;
  --text:#555;
  --muted:#bbb;
  --light:#f3f3f3;
  --white:#fff;
}
*{box-sizing:border-box;margin:0;padding:0}
html,body{width:1200px;height:4292px;overflow:hidden}
body{position:relative;font-family:"Roboto",Arial,sans-serif;color:var(--text);background:var(--white)}
.abs{position:absolute}
.heading{font-family:"Barlow",Arial,sans-serif;font-weight:900;color:var(--ink);text-transform:uppercase;letter-spacing:-.5px}
.heading em{font-style:normal;color:var(--green)}
.rule{position:absolute;height:3px;width:63px;background:var(--green)}
.btn{position:absolute;background:var(--green);color:#fff;font-family:"Barlow",sans-serif;font-weight:800;font-size:13px;text-transform:uppercase;display:flex;align-items:center;justify-content:center;gap:6px;border-radius:2px}
.circle-arrow{position:absolute;width:32px;height:32px;border-radius:50%;display:flex;align-items:center;justify-content:center}

/* header */
.topbar{left:525px;top:0;width:675px;height:33px;background:var(--green);clip-path:polygon(32px 0,100% 0,100% 100%,0 100%);color:#fff;font-size:12px;display:flex;align-items:center;gap:30px;padding-left:72px}
.topbar span{display:flex;align-items:center;gap:8px}
.logo{left:110px;top:18px;font-family:"Barlow",sans-serif;font-weight:900;font-size:27px;line-height:26px;color:var(--ink);width:140px}
.nav{left:560px;top:52px;display:flex;gap:26px;font-size:13px;color:var(--ink)}
.nav .active{color:var(--green)}

/* hero */
.hero{left:0;top:85px;width:1200px;height:643px;background:linear-gradient(100deg,#c9cfc9 0%,#d6d2c6 30%,#8b5b46 60%,#7f6f5d 100%)}
.hero-title{left:645px;top:272px;font-size:50px;line-height:52px}

/* features */
.features{left:0;top:728px;width:1200px;height:307px;display:flex}
.feature{flex:1;background:var(--dark);color:#fff;text-align:center;padding-top:38px}
.feature.green{background:var(--green)}
.feature .icon{width:83px;height:83px;border-radius:50%;background:#fff;margin:0 auto;display:flex;align-items:center;justify-content:center}
.feature h3{font-family:"Barlow",sans-serif;font-weight:800;font-size:20px;text-transform:uppercase;margin-top:24px}
.feature p{font-size:12.5px;line-height:22px;width:300px;margin:12px auto 0}

/* about */
.about-text{left:112px;width:458px;font-size:13px;line-height:21.5px;text-align:justify}
.about-photo{left:643px;top:1150px;width:432px;height:408px;background:linear-gradient(160deg,#6e7f8e,#9a8f70 45%,#3f6b2e);border:1px solid #fff}
.frame{left:667px;top:1113px;width:446px;height:179px;border:17px solid var(--green);border-left:none;border-bottom:none;border-radius:0 8px 0 0}

/* services */
.services-band{left:0;top:1673px;width:1200px;height:352px;background:var(--green)}
.services-grey{left:0;top:2025px;width:1200px;height:192px;background:var(--light)}
.service{position:absolute;top:1868px;width:230px}
.service .ph{height:237px}
.service p{text-align:center;font-size:20px;font-weight:500;color:var(--ink);margin-top:14px}

/* why */
.why-photo{left:0;top:2230px;width:552px;height:453px;border-radius:0 260px 260px 0;background:var(--green);padding:12px 10px 0 0}
.why-photo div{width:100%;height:100%;border-radius:0 250px 250px 0;background:linear-gradient(110deg,#b4473b,#e08a37 40%,#c2c8cc 80%)}
.why-list{left:602px;top:2325px;width:500px;list-style:none}
.why-list li{display:flex;gap:14px;font-size:13px;line-height:21px;height:65px}
.why-list svg{flex:none;margin-top:4px}

/* testimonials */
.testi{position:absolute;text-align:center}
.avatar{width:75px;height:75px;border-radius:50%;margin:0 auto;border:3px solid var(--green);background:radial-gradient(circle at 50% 40%,#e0d6cc,#9aa2a8)}
.testi h4{font-size:19px;font-weight:500;color:var(--ink);margin-top:10px}
.stars{color:var(--green);font-size:17px;letter-spacing:4px;margin-top:2px}
.testi p{font-size:13px;line-height:21.5px;margin-top:8px}
.faded{opacity:.35}
.faded .avatar{border-color:#ccc}

/* contact */
.map{left:0;top:3375px;width:1200px;height:508px;background:linear-gradient(135deg,#d3e4c4,#e9e6d6 40%,#cfe0bd 70%,#e3e9d8)}
.contact-panel{left:600px;top:3463px;width:600px;height:329px;background:var(--green);clip-path:polygon(83px 0,100% 0,100% 100%,0 100%)}
.contact-item{left:730px;display:flex;gap:16px;color:#fff;font-size:13.5px;line-height:26px}
.contact-item .ic{width:32px;height:32px;border-radius:50%;background:#fff;display:flex;align-items:center;justify-content:center;flex:none;margin-top:4px}

/* footer */
.footer{left:0;top:3883px;width:1200px;height:409px;background:var(--ink);color:#fff}
.f-logo{left:110px;top:3990px;font-family:"Barlow",sans-serif;font-weight:900;font-size:32px;color:#fff}
.f-title{font-size:20px;font-weight:500;color:#fff}
.f-links{list-style:none;font-size:13px;line-height:26px;color:#fff}
.f-links li::before{content:"›";margin-right:14px}
.email{left:110px;top:4100px;width:313px;height:42px;background:#fff;border:2px solid var(--green);display:flex;align-items:center;font-size:13px;color:#777;padding-left:18px}
.email .send{position:absolute;right:0;top:0;width:42px;height:38px;background:var(--green);display:flex;align-items:center;justify-content:center}
.copy{left:0;top:4237px;width:1200px;text-align:center;font-size:12px;color:#fff}
</style>
</head>
<body>

<!-- Header -->
<div class="abs topbar">
  <span><svg width="16" height="16" viewBox="0 0 16 16"><circle cx="8" cy="8" r="8" fill="#fff"/><rect x="4" y="5" width="8" height="6" fill="none" stroke="#4c9f38" stroke-width="1.2"/><path d="M4 5l4 3 4-3" fill="none" stroke="#4c9f38" stroke-width="1.2"/></svg>Mail Today : info@companyname.com</span>
  <span><svg width="16" height="16" viewBox="0 0 16 16"><circle cx="8" cy="8" r="8" fill="#fff"/><path d="M5 4.5l2 0 .8 2-1 .8a5 5 0 0 0 2 2l.8-1 2 .8v2a1 1 0 0 1-1 1A7 7 0 0 1 4 5.5a1 1 0 0 1 1-1z" fill="#4c9f38"/></svg>Call Us Today : +1 888 888 8888</span>
</div>
<div class="abs logo">JUNK<br>REMOVAL</div>
<nav class="abs nav"><span class="active">Home</span><span>Who We Are</span><span>What We Remove</span><span>Our Work</span><span>Blog</span><span>FAQ</span><span>Contact us</span></nav>

<!-- Hero -->
<div class="abs hero" role="img" aria-label="Smiling worker in high-visibility jacket giving a thumbs up beside a blue wheelie bin"></div>
<h1 class="abs heading hero-title">We Make Junk<br><em>Disappear.</em></h1>
<div class="btn" style="left:645px;top:393px;width:150px;height:37px">Get Started</div>
<div class="circle-arrow" style="left:657px;top:601px;background:#222"><svg width="10" height="12"><path d="M7 1L2 6l5 5" stroke="#fff" stroke-width="2" fill="none"/></svg></div>
<div class="circle-arrow" style="left:707px;top:601px;background:#222"><svg width="10" height="12"><path d="M3 1l5 5-5 5" stroke="#fff" stroke-width="2" fill="none"/></svg></div>

<!-- Features -->
<section class="abs features">
  <div class="feature">
    <div class="icon"><svg width="40" height="40" viewBox="0 0 40 40" fill="none" stroke="#4c9f38" stroke-width="2"><path d="M20 34s-10-11-10-18a10 10 0 0 1 20 0c0 7-10 18-10 18z"/><circle cx="20" cy="16" r="4"/></svg></div>
    <h3>Find A Location</h3>
    <p>Lorem ipsum dolor sit amet, consectetur adipiscing elit, sed do eiusmod tempor incididunt ut labore et dolore magna aliqua.</p>
  </div>
  <div class="feature green">
    <div class="icon"><svg width="40" height="40" viewBox="0 0 40 40" fill="none" stroke="#4c9f38" stroke-width="2"><circle cx="18" cy="20" r="11"/><path d="M21 15h-4a2.5 2.5 0 0 0 0 5h2a2.5 2.5 0 0 1 0 5h-4M18 12v3M18 25v3"/></svg></div>
    <h3>Our Pricing</h3>
    <p>Lorem ipsum dolor sit amet, consectetur adipiscing elit, sed do eiusmod tempor incididunt ut labore et dolore magna aliqua.</p>
  </div>
  <div class="feature">
    <div class="icon"><svg width="40" height="40" viewBox="0 0 40 40" fill="none" stroke="#4c9f38" stroke-width="2"><rect x="6" y="8" width="28" height="19" rx="1"/><path d="M15 33h10M20 27v6M11 14h10M11 19h14"/></svg></div>
    <h3>Get A Free Quote Online</h3>
    <p>Lorem ipsum dolor sit amet, consectetur adipiscing elit, sed do eiusmod tempor incididunt ut labore et dolore magna aliqua.</p>
  </div>
</section>

<!-- Who we are -->
<h2 class="abs heading" style="left:112px;top:1128px;font-size:37px">Who <em>We</em> Are</h2>
<div class="rule" style="left:112px;top:1196px"></div>
<p class="abs about-text" style="top:1218px">Lorem ipsum dolor sit amet, consectetur adipiscing elit, sed do eiusmod tempor incididunt ut labore et dolore magna aliqua. Ut enim ad minim veniam, quis nostrud exercitation ullamco laboris nisi ut aliquip ex ea commodo consequat. Duis aute irure dolor in reprehenderit in voluptate velit esse cillum dolore eu fugiat nulla pariatur.</p>
<p class="abs about-text" style="top:1347px">Excepteur sint occaecat cupidatat non proident, sunt in culpa qui officia deserunt mollit anim id est laborum. Lorem ipsum dolor sit amet, consectetur adipiscing elit, sed do eiusmod tempor incididunt ut labore et dolore magna aliqua. Ut enim ad minim veniam, quis nostrud exercitation ullamco laboris nisi ut aliquip ex ea commodo consequat. Duis aute irure dolor in reprehenderit in voluptate velit esse cillum dolore eu fugiat nulla pariatur. Excepteur sint occaecat cupidatat non proident, sunt in culpa qui officia deserunt mollit anim id est laborum.</p>
<div class="btn" style="left:112px;top:1533px;width:150px;height:38px">Learn More <svg width="12" height="12"><circle cx="6" cy="6" r="6" fill="#fff"/><path d="M5 3l3 3-3 3" stroke="#4c9f38" stroke-width="1.6" fill="none"/></svg></div>
<div class="abs frame"></div>
<div class="abs about-photo" role="img" aria-label="Two workers in safety gear loading a yellow bin into a green garbage truck"></div>

<!-- Services -->
<div class="abs services-band"></div>
<div class="abs services-grey"></div>
<h2 class="abs heading" style="left:0;width:1200px;top:1768px;font-size:37px;color:#fff;text-align:center">Our Services</h2>
<div class="rule" style="left:568px;top:1834px;background:#fff"></div>
<div class="circle-arrow" style="left:41px;top:1944px;background:#6fb45d"><svg width="10" height="12"><path d="M7 1L2 6l5 5" stroke="#fff" stroke-width="2" fill="none"/></svg></div>
<div class="circle-arrow" style="left:1128px;top:1944px;background:#6fb45d"><svg width="10" height="12"><path d="M3 1l5 5-5 5" stroke="#fff" stroke-width="2" fill="none"/></svg></div>
<div class="service" style="left:110px"><div class="ph" role="img" aria-label="Family carrying cardboard moving boxes" style="background:linear-gradient(160deg,#d9d2c6,#b9a27e)"></div><p>Moving</p></div>
<div class="service" style="left:360px"><div class="ph" role="img" aria-label="Worker in orange uniform with a blue wheelie bin" style="background:linear-gradient(160deg,#c9c1b2,#e39a3a 55%,#2f6cb8)"></div><p>Junk Removal</p></div>
<div class="service" style="left:610px"><div class="ph" role="img" aria-label="Worker standing in front of an orange garbage truck" style="background:linear-gradient(160deg,#e58a2c,#c65d1e 50%,#2d2f32)"></div><p>Hourly Services</p></div>
<div class="service" style="left:860px"><div class="ph" role="img" aria-label="Workers loading green bins into a garbage truck" style="background:linear-gradient(160deg,#5f8f45,#8d9a86 55%,#3f6e36)"></div><p>Multiservices</p></div>

<!-- Why choose us -->
<div class="abs why-photo"><div role="img" aria-label="Smiling worker in orange uniform giving a thumbs up by a truck"></div></div>
<h2 class="abs heading" style="left:602px;top:2233px;font-size:37px">Why <em>Choose</em> Us</h2>
<div class="rule" style="left:602px;top:2301px"></div>
<ul class="abs why-list">
  <li><svg width="14" height="14"><circle cx="7" cy="7" r="7" fill="#4c9f38"/><path d="M4 7l2 2 4-4" stroke="#fff" stroke-width="1.6" fill="none"/></svg>Lorem ipsum dolor sit amet, consectetur adipiscing elit, sed do eiusmod tempor incididunt ut labore et dolore magna aliqua.</li>
  <li><svg width="14" height="14"><circle cx="7" cy="7" r="7" fill="#4c9f38"/><path d="M4 7l2 2 4-4" stroke="#fff" stroke-width="1.6" fill="none"/></svg>Ut enim ad minim veniam, quis nostrud exercitation ullamco laboris nisi ut aliquip ex ea commodo consequat.</li>
  <li><svg width="14" height="14"><circle cx="7" cy="7" r="7" fill="#4c9f38"/><path d="M4 7l2 2 4-4" stroke="#fff" stroke-width="1.6" fill="none"/></svg>Duis aute irure dolor in reprehenderit in voluptate velit esse cillum dolore eu fugiat nulla pariatur.</li>
  <li><svg width="14" height="14"><circle cx="7" cy="7" r="7" fill="#4c9f38"/><path d="M4 7l2 2 4-4" stroke="#fff" stroke-width="1.6" fill="none"/></svg>Excepteur sint occaecat cupidatat non proident, sunt in culpa qui officia deserunt mollit anim id est laborum.</li>
  <li><svg width="14" height="14"><circle cx="7" cy="7" r="7" fill="#4c9f38"/><path d="M4 7l2 2 4-4" stroke="#fff" stroke-width="1.6" fill="none"/></svg>Lorem ipsum dolor sit amet, consectetur adipiscing elit, sed do eiusmod tempor incididunt ut labore et dolore magna aliqua.</li>
</ul>
<div class="btn" style="left:602px;top:2642px;width:150px;height:38px">Learn More <svg width="12" height="12"><circle cx="6" cy="6" r="6" fill="#fff"/><path d="M5 3l3 3-3 3" stroke="#4c9f38" stroke-width="1.6" fill="none"/></svg></div>

<!-- Testimonials -->
<h2 class="abs heading" style="left:0;width:1200px;top:2880px;font-size:37px;text-align:center">Hear From Our <em>Happy Clients</em></h2>
<div class="abs" style="left:300px;top:2960px;font-family:Georgia,serif;font-size:300px;line-height:300px;color:#eef3ec">“</div>
<div class="testi faded" style="left:-40px;top:3048px;width:300px">
  <div class="avatar" role="img" aria-label="Client portrait"></div>
  <h4>John Doe</h4><div class="stars">★★★★★</div>
  <p>Lorem ipsum dolor sit amet, consectetur adipiscing elit, sed do eiusmod tempor incididunt ut labore et dolore magna aliqua. Ut enim ad minim veniam, quis nostrud exercitation ullamco laboris commodo consequat.</p>
</div>
<div class="testi faded" style="left:895px;top:3048px;width:300px">
  <div class="avatar" role="img" aria-label="Client portrait"></div>
  <h4>John Doe</h4><div class="stars">★★★★★</div>
  <p>Lorem ipsum dolor sit amet, consectetur adipiscing elit, sed do eiusmod tempor incididunt ut labore et dolore magna aliqua. Ut enim ad minim veniam, quis nostrud exercitation ullamco laboris commodo consequat.</p>
</div>
<div class="testi" style="left:383px;top:2980px;width:434px">
  <div class="avatar" role="img" aria-label="Client portrait"></div>
  <h4>John Doe</h4><div class="stars">★★★★★</div>
  <p>Lorem ipsum dolor sit amet, consectetur adipiscing elit, sed do eiusmod tempor incididunt ut labore et dolore magna aliqua. Ut enim ad minim veniam, quis nostrud exercitation ullamco laboris nisi ut aliquip ex ea commodo consequat.</p>
</div>
<div class="circle-arrow" style="left:111px;top:3141px;background:#222"><svg width="10" height="12"><path d="M7 1L2 6l5 5" stroke="#fff" stroke-width="2" fill="none"/></svg></div>
<div class="circle-arrow" style="left:1054px;top:3141px;background:var(--green)"><svg width="10" height="12"><path d="M3 1l5 5-5 5" stroke="#fff" stroke-width="2" fill="none"/></svg></div>

<!-- Contact -->
<div class="abs map" role="img" aria-label="Road map of the western United States"></div>
<div class="abs contact-panel"></div>
<h2 class="abs heading" style="left:730px;top:3505px;font-size:37px;color:#fff">Contact Us</h2>
<div class="rule" style="left:730px;top:3570px;background:#fff"></div>
<div class="abs contact-item" style="top:3582px"><div class="ic"><svg width="14" height="16" viewBox="0 0 14 16"><path d="M7 15s-5-5-5-9a5 5 0 0 1 10 0c0 4-5 9-5 9z" fill="#4c9f38"/><circle cx="7" cy="6" r="2" fill="#fff"/></svg></div><div>Lorem ipsum dolor sit amet,<br>consectetur</div></div>
<div class="abs contact-item" style="top:3642px"><div class="ic"><svg width="14" height="14" viewBox="0 0 16 16"><path d="M3 2l3 0 1 3-1.5 1.2a7 7 0 0 0 3.3 3.3L10 8l3 1v3a1.5 1.5 0 0 1-1.5 1.5A10 10 0 0 1 1.5 3.5 1.5 1.5 0 0 1 3 2z" fill="#4c9f38"/></svg></div><div>Phone :<br>+1 888 888 8888</div></div>
<div class="abs contact-item" style="top:3702px"><div class="ic"><svg width="14" height="12" viewBox="0 0 14 12"><rect width="14" height="12" rx="1" fill="#4c9f38"/><path d="M1 1l6 5 6-5" stroke="#fff" stroke-width="1.4" fill="none"/></svg></div><div>Email :<br>info@companyname.com</div></div>

<!-- Footer -->
<div class="abs footer"></div>
<div class="abs f-logo">JUNK REMOVAL</div>
<p class="abs" style="left:110px;top:4033px;width:320px;font-size:13.5px;line-height:27px;color:#fff">Here you'll find regular market updates, expert tips &amp; stories.</p>
<div class="abs email">Email address<div class="send"><svg width="14" height="14" viewBox="0 0 14 14"><path d="M13 1L1 6l5 2 2 5z" fill="#fff"/></svg></div></div>
<h4 class="abs f-title" style="left:542px;top:3980px">Useful Links</h4>
<ul class="abs f-links" style="left:542px;top:4024px"><li>About Us</li><li>Meet Our Team</li><li>Our Accounts</li><li>Platform</li><li>Site Search</li><li>Accessibility</li></ul>
<ul class="abs f-links" style="left:695px;top:4024px"><li>Privacy Policy</li><li>Terms &amp; Conditions</li><li>Blog</li><li>Faq</li><li>Contact</li></ul>
<h4 class="abs f-title" style="left:900px;top:3980px">Contact Us</h4>
<div class="abs" style="left:900px;top:4024px;display:flex;gap:20px;font-size:13px;line-height:26px;color:#fff"><svg width="10" height="14" viewBox="0 0 14 16" style="margin-top:6px"><path d="M7 15s-5-5-5-9a5 5 0 0 1 10 0c0 4-5 9-5 9z" fill="#4c9f38"/></svg><div>Lorem ipsum dolor sit amet,<br>consectetur</div></div>
<div class="abs" style="left:900px;top:4102px;display:flex;gap:20px;font-size:13px;line-height:26px;color:#fff"><svg width="12" height="12" viewBox="0 0 16 16" style="margin-top:7px"><path d="M3 2l3 0 1 3-1.5 1.2a7 7 0 0 0 3.3 3.3L10 8l3 1v3a1.5 1.5 0 0 1-1.5 1.5A10 10 0 0 1 1.5 3.5 1.5 1.5 0 0 1 3 2z" fill="#4c9f38"/></svg><div>+1 888 888 8888</div></div>
<div class="abs" style="left:900px;top:4154px;display:flex;gap:20px;font-size:13px;line-height:26px;color:#fff"><svg width="13" height="11" viewBox="0 0 14 12" style="margin-top:8px"><rect width="14" height="12" rx="1" fill="#4c9f38"/><path d="M1 1l6 5 6-5" stroke="#1f1f1f" stroke-width="1.4" fill="none"/></svg><div>info@companyname.com</div></div>
<div class="abs" style="left:0;top:4215px;width:1200px;height:1px;background:#333"></div>
<p class="abs copy">Copyrights © 2023 Company name. All Rights Reserved. &nbsp;| &nbsp;Privacy policy</p>

</body>
</html>
```